Consumer Credit Attorney Needs Logo for Letterhead & Business cards

I need a basic logo or letterhead design for a new law firm in Mobile, Alabama. The firm is called "Marlow T. Fenwick, PC." We represent people fighting large corporations in cases involving Fair Credit Reporting, Debt Collection, Mortgage Fraud, Truth in Lending, and Wrongful Foreclosures. I don't want anything with scales of justice or columns or the typical lawyer imagery. I ride a bike to court. I keep most of my office in the cloud. I'm a different type of lawyer, and I want a design that is simple, elegant, and made primarily of blue and white.

The Job is now Payment Committed.  I look forward to seeing your submissions.  Thanks1

Reason: I have just recently received some new designs and provided feedback on them. You all deserve some time to consider the feedback. Thanks!

• Clear lines and a small footprint on the letterhead. I like several antique styles- Gilded Age, Rococo, Edwardian, even Art Deco.
• The only thing I hate is 1990s clip-art style graphics. No illustrations of money, courthouses, scales, columns, etc. I also hate silly fonts, overly fancy or "handwritten" fonts, and Arial font.

```html
<!DOCTYPE html>
<html lang="en">
<head>
<meta charset="utf-8">
<title>Marlow T. Fenwick, PC — Letterhead</title>
<link href="https://fonts.googleapis.com/css2?family=Questrial&display=swap" rel="stylesheet">
<style>
  :root {
    --backdrop: #e3e4e5;
    --paper: #f7f7f7;
    --brand-blue: #1f5879;
    --ink-grey: #5a5f63;
  }
  * { margin: 0; padding: 0; box-sizing: border-box; }
  html, body { width: 1200px; height: 968px; overflow: hidden; }
  body {
    position: relative;
    background: var(--backdrop);
    font-family: "Questrial", sans-serif;
  }
  .letterhead {
    position: absolute;
    left: 120px; top: 40px;
    width: 660px; height: 854px;
    background: var(--paper);
    box-shadow: 0 2px 10px rgba(0,0,0,0.12);
  }
  .letterhead__header {
    position: absolute;
    right: 48px; top: 54px;
    text-align: right;
  }
  .firm-name {
    display: flex; align-items: center; justify-content: flex-end; gap: 10px;
    font-family: "Questrial", sans-serif;
    font-weight: 400;
    color: var(--brand-blue);
    font-size: 22px;
    line-height: 1;
  }
  .firm-name__dot {
    width: 14px; height: 14px;
    border-radius: 50%;
    background: var(--brand-blue);
  }
  .firm-web {
    margin-top: 8px;
    font-size: 10px;
    letter-spacing: 4px;
    color: var(--ink-grey);
  }
  .letterhead__footer {
    position: absolute;
    left: 48px; right: 48px; bottom: 58px;
  }
  .contact {
    font-size: 9px;
    line-height: 14px;
    color: var(--ink-grey);
  }
  .contact__label { color: var(--brand-blue); }
  .footer-rule {
    margin-top: 8px;
    height: 3px;
    background: var(--brand-blue);
  }
  .brand-lockup {
    position: absolute;
    right: 44px; bottom: 62px;
    display: flex; align-items: center; gap: 12px;
    font-family: "Questrial", sans-serif;
    font-weight: 400;
    color: var(--brand-blue);
    font-size: 28px;
    line-height: 1;
  }
  .brand-lockup__dot {
    width: 20px; height: 20px;
    border-radius: 50%;
    background: var(--brand-blue);
  }
</style>
</head>
<body>
  <section class="letterhead">
    <header class="letterhead__header">
      <div class="firm-name"><span class="firm-name__dot"></span>Marlow T. Fenwick, PC.</div>
      <div class="firm-web">www.marlowfenwick.com</div>
    </header>
    <footer class="letterhead__footer">
      <p class="contact">2210 Dauphin St. Suite 4, Mobile, AL 36606</p>
      <p class="contact">
        <span class="contact__label">T:</span> 251-555-0148 ·
        <span class="contact__label">F:</span> 251-555-0193 ·
        <span class="contact__label">E:</span> info@marlowfenwick.com
      </p>
      <div class="footer-rule"></div>
    </footer>
  </section>

  <div class="brand-lockup"><span class="brand-lockup__dot"></span>Marlow T. Fenwick, PC.</div>
</body>
</html>
```